Sponsorship and registration document for Charity Golf Day 2022

The project requires 2 documents to be updated to look more graphically savvy and professionally presentable.
1. Charity golf day sponsorship document
2. One page registration document.
The text has been completed. Text not to be changed - just graphics.
New images would be preferred.
The logos have been provided.

Target Market(s)

Corporate Sponsors and Golf players

Requirements
Must have
• Golf Theme

```html
<!DOCTYPE html>
<html lang="en">
<head>
<meta charset="utf-8">
<title>Charity Golf Day – Sponsorship Proposal</title>
<link href="https://fonts.googleapis.com/css2?family=Montserrat:wght@300;400;500;600;700;800&display=swap" rel="stylesheet">
<style>
:root{
  --green:#8fce4c;
  --blue:#2f5597;
  --ink:#333;
  --gold:#f2a900;
  --border:#222;
}
*{box-sizing:border-box;margin:0;padding:0}
html,body{width:923px;height:1200px;overflow:hidden;background:#fff}
body{position:relative;font-family:'Montserrat',sans-serif;color:var(--ink)}
.page{position:absolute;width:515px;height:665px;border:2px solid var(--border);background:#fff;transform:scale(.5494);transform-origin:0 0;overflow:hidden;font-size:8.6px;line-height:14.5px;font-weight:400}
.abs{position:absolute}
.topbar{position:absolute;left:0;top:12px;width:100%;height:17px;background:var(--green);color:#fff;font-size:6.8px;font-weight:500;letter-spacing:.2px}
.topbar .doc{position:absolute;left:0;top:0;height:17px;width:215px;background:var(--blue);clip-path:polygon(0 0,205px 0,215px 50%,205px 100%,0 100%);text-align:center;line-height:17px;padding-right:10px}
.topbar .sec{position:absolute;left:215px;width:300px;text-align:center;line-height:17px;padding-right:40px}
.topbar .num{position:absolute;right:28px;line-height:17px}
.blue{color:var(--blue)}
.green{color:var(--green)}
h3.sub{color:var(--blue);font-size:8.6px;font-weight:700;margin:12px 0 2px}
.flags{list-style:none}
.flags li{position:relative;padding-left:15px}
.flags li::before{content:"";position:absolute;left:6px;top:3px;width:1px;height:8px;background:var(--green)}
.flags li::after{content:"";position:absolute;left:7px;top:3px;border-left:6px solid var(--green);border-top:2.5px solid transparent;border-bottom:2.5px solid transparent}
.dots{list-style:none}
.dots li{position:relative;padding-left:10px}
.dots li::before{content:"";position:absolute;left:2px;top:5px;width:4px;height:4px;border-radius:50%;background:var(--green)}
.sechead{display:flex;align-items:center;gap:8px;color:var(--blue);font-size:12.5px;font-weight:500;white-space:nowrap}
.sechead::before,.sechead::after{content:"";flex:1;height:1.5px;background:var(--blue)}
.tier{color:var(--green);font-size:10.5px;font-weight:500;margin-top:8px}
.field{display:flex;align-items:flex-end;font-size:7.8px;margin-bottom:9px}
.field .line{flex:1;border-bottom:1px dotted #666;margin-left:3px;height:9px}
.field.short .line{flex:0 0 90px}
.player b{font-weight:700}
.note{color:var(--blue);font-size:7.6px;line-height:19px}
.cornerbox{position:absolute;border:2px solid var(--green)}
.cornerbox i{position:absolute;width:0;height:0}
.cornerbox .tl{left:6px;top:6px;border-top:16px solid var(--green);border-right:16px solid transparent}
.cornerbox .tr{right:6px;top:6px;border-top:16px solid var(--green);border-left:16px solid transparent}
.cornerbox .bl{left:6px;bottom:6px;border-bottom:16px solid var(--green);border-right:16px solid transparent}
.cornerbox .br{right:6px;bottom:6px;border-bottom:16px solid var(--green);border-left:16px solid transparent}
.toc-row{display:flex;align-items:flex-end;font-size:10px;font-weight:500;margin-bottom:6.5px}
.toc-row .lead{flex:1;border-bottom:1.5px solid var(--green);margin:0 6px 3px}
.flaghead{display:flex;align-items:center;gap:10px;color:var(--blue);font-size:14px;font-weight:600}
.kv{display:grid;grid-template-columns:62px 1fr;font-size:7.6px;line-height:10px;font-weight:500}
.check{display:inline-block;width:9px;height:7px;border:1px solid #444;margin-right:5px;vertical-align:middle}
</style>
</head>
<body>

<!-- Page: Cover -->
<section class="page" style="left:22px;top:34px">
  <div class="abs" style="left:0;top:0;width:515px;height:150px;background:var(--green)"></div>
  <div class="abs" role="img" aria-label="White silhouette of a golfer finishing a swing" style="left:62px;top:22px;width:170px;height:100px;background:linear-gradient(180deg,#a6d96d,#9bd35d);border-radius:4px"></div>
  <div class="abs" style="left:240px;top:18px;color:var(--blue);font-size:43px;font-weight:800;line-height:40px;letter-spacing:.5px">CHARITY<br>GOLF DAY</div>
  <div class="abs" style="left:246px;top:100px;color:#fff;font-size:9.5px;line-height:14px;font-weight:400">Friday 25 March 2022 | Elmwood Golf Club<br>www.riverbendclub.org/golf-day</div>
  <div class="abs" style="left:0;top:150px;width:515px;height:40px;background:var(--blue);color:#fff;font-size:21px;font-weight:700;text-align:center;line-height:40px;padding-right:20px">SPONSORSHIP PROPOSAL</div>
  <div class="abs" role="img" aria-label="Golf course with sand bunkers, green fairway and trees by the sea" style="left:0;top:190px;width:515px;height:205px;background:linear-gradient(180deg,#6d8fa8 0%,#5a7a5a 22%,#d7cbb0 45%,#c9bea2 58%,#5f8f3a 75%,#4d7d2c 100%)"></div>
  <div class="abs" style="left:430px;top:188px;border-top:16px solid var(--blue);border-left:16px solid transparent;border-right:16px solid transparent"></div>
  <div class="abs" style="left:56px;top:380px;border-bottom:16px solid var(--blue);border-left:16px solid transparent;border-right:16px solid transparent"></div>
  <div class="abs" style="left:0;top:396px;width:515px;height:37px;background:var(--blue);color:#fff;font-size:14.5px;font-weight:500;text-align:center;line-height:37px;padding-right:20px">Supporting Prostate Cancer Research</div>
  <div class="cornerbox" style="left:60px;top:468px;width:395px;height:110px"><i class="tl"></i><i class="tr"></i><i class="bl"></i><i class="br"></i>
    <p style="color:var(--green);font-size:15px;line-height:24px;text-align:center;margin-top:19px">Help us hit prostate cancer off the green<br>and beat the most common cancer<br>in Australian men.</p>
  </div>
  <div class="abs" style="left:200px;top:610px;display:flex;align-items:center;gap:6px">
    <span style="color:var(--blue);font-size:15px;font-weight:600">Riverbend Club</span>
    <span style="width:22px;height:22px;border-radius:50%;background:var(--gold)"></span>
  </div>
</section>

<!-- Page: Contents -->
<section class="page" style="left:324px;top:34px">
  <div class="topbar"><span class="doc">CHARITY GOLF DAY</span><span class="sec">SPONSORSHIP PROPOSAL</span></div>
  <div class="abs" style="left:30px;top:100px;width:375px">
    <div class="flaghead"><svg width="14" height="16" viewBox="0 0 14 16"><path d="M1 0v16" stroke="#2f5597" stroke-width="1.6"/><path d="M2 1l11 4-11 4z" fill="#2f5597"/></svg>Contents</div>
    <div style="margin:10px 0 0 22px">
      <div class="toc-row">Charity Golf Day Invitation<span class="lead"></span>2</div>
      <div class="toc-row">About Prostate Cancer<span class="lead"></span>3</div>
      <div class="toc-row">Why are we asking you to be involved<span class="lead"></span>3</div>
      <div class="toc-row">What to expect<span class="lead"></span>4</div>
      <div class="toc-row">Sponsorship Opportunities<span class="lead"></span>5</div>
      <div class="toc-row">Application Form<span class="lead"></span>7</div>
    </div>
  </div>
  <div class="abs" style="left:30px;top:358px;width:400px">
    <div class="flaghead"><svg width="14" height="16" viewBox="0 0 14 16"><path d="M1 0v16" stroke="#2f5597" stroke-width="1.6"/><path d="M2 1l11 4-11 4z" fill="#2f5597"/></svg>Contact</div>
    <div style="margin:10px 0 0 22px;font-size:7.6px;line-height:10px;font-weight:500">
      <p>Mara Ellison<br>Convenor<br>Co - President, Riverbend Service Club</p>
      <div class="kv"><span>Mobile</span><span>: 0412 555 018</span><span>Email</span><span>: <span class="blue">mara.ellison@mailbox.example</span></span><span>Web</span><span>: <span class="blue">www.riverbendclub.org/golf-day</span></span></div>
      <p style="margin-top:20px">Nadia Corvell<br>Event Manager<br>Email : <span class="blue">nadia.corvell@mailbox.example</span></p>
    </div>
  </div>
</section>

<!-- Page 2: Invitation -->
<section class="page" style="left:624px;top:34px">
  <div class="topbar"><span class="doc">CHARITY GOLF DAY</span><span class="sec">SPONSORSHIP PROPOSAL</span><span class="num">2</span></div>
  <div class="abs" style="left:42px;top:52px;width:435px;font-size:7.7px;line-height:13.5px;text-align:justify">
    <p class="blue" style="font-size:11.5px;line-height:15px;font-weight:600;text-align:left;margin-bottom:16px">Join us for an exclusive day on the private Elmwood Golf Course, with all proceeds going to support Prostate Cancer Research, Awareness and Support.</p>
    <p>The Riverbend Service Club will again be holding its Charity Golf Day with all proceeds used to support the Prostate Cancer Research, awareness and Support Programs. The venue will be the prestigious Elmwood Golf Club on Friday 25 March 2022, with a shotgun start at 8:00 am.</p>
    <p style="margin-top:12px">We have enclosed for your information a copy of our promotional sponsor packages that outline the event, sponsorship package options and inclusions.</p>
    <p style="margin-top:12px">The format of the day involves:</p>
    <ul class="flags"><li>Player registration, refreshments and light breakfast from 7:00am</li><li>Ambrose competition starting at 8:00am</li><li>Two Course lunch and presentations in the club house from 12:30pm</li></ul>
    <p style="margin-top:12px">Your commitment to supporting health programs in our community is truly appreciated. With assistance from sponsors such as yourself, we will continue to see improvements in the support and treatment for men and their families with prostate cancer.</p>
    <p style="margin-top:12px">We hope that you will consider supporting the worthwhile event that is open to any organisation or individual who wishes to enjoy the benefits of playing golf at the prestigious Elmwood Golf Club.</p>
    <p style="margin-top:12px">For more information, please check the website ( www.riverbendclub.org/golf-day) or should you wish to discuss any aspect of the event, please contact me on 0412 555 018.</p>
    <p style="margin-top:22px">Yours sincerely</p>
    <p style="margin-top:30px;line-height:13.5px"><b class="blue" style="font-weight:600">Mara Ellison<br>Convener</b><br>Co - President 2021 -2022<br>Secretary 2021 - 2022<br>Riverbend Service Club</p>
  </div>
</section>

<!-- Page 3: About prostate cancer -->
<section class="page" style="left:15px;top:418px">
  <div class="topbar"><span class="doc">CHARITY GOLF DAY</span><span class="sec">SPONSORSHIP PROPOSAL</span><span class="num">3</span></div>
  <div class="abs" style="left:42px;top:52px;width:435px;font-size:7.7px;line-height:13.5px;text-align:justify">
    <h3 class="sub" style="margin-top:0">Why prostate cancer?</h3>
    <ul class="flags"><li>Prostate cancer is the most diagnosed cancer in Australian men.</li><li>Approximately 20,000 Australian men are diagnosed with prostate cancer each year.</li><li>Over 200,000 Australian men are living with a diagnosis prostate cancer.</li><li>95% of Australian men diagnosed with prostate cancer survive for at least 5 years.</li><li>Almost 3,500 Australian men die of prostate cancer each year.</li></ul>
    <h3 class="sub">Why are we asking you to be involved?</h3>
    <ul class="flags"><li>Every day 54 Australian men will be told they have prostate cancer</li><li>70% of research applications are unfunded</li><li>1 in 6 men will suffer from prostate cancer</li><li>9 families lose a loved one to prostate cancer every day</li><li>Only 1 in 3 men have access to a specialist nurse</li></ul>
    <h3 class="sub">What this fundraising event can achieve</h3>
    <ul class="flags" style="text-align:left"><li><span class="green">$12,500</span> – Could provide funding for a researcher working for one month on a project to reduce side – effects post treatment.</li><li><span class="green">$30,000</span> – could provide finding for a senior scientist for three months working on a project to improve treatments for prostate cancer that has spread to the bones.</li><li><span class="green">$50,000</span> – could fund a project to improve early – diagnosis for men with a family history of prostate cancer.</li></ul>
    <p style="margin-top:13px">Proceeds from this event will be donated to Prostate Cancer Research Group at the Institute for Medical Discovery, Eastfield University, to fund world leading, innovative research and to support men and their families affected by prostate cancer.</p>
    <p style="margin-top:13px">Their innovative research program has a strong translational approach, involving lab-based studies with tissues donated by patients with prostate cancer. Their collaborative studies with clinicians and patient advocates address questions that are relevant to patient care. The findings have the potential to improve the management and outcomes of men with different stages of prostate cancer. Recent studies have informed international guidelines for diagnosis of prostate cancer and led to new clinical trials.</p>
    <p style="margin-top:13px">For more information visit their website www.eastfield.edu/medical-discovery/prostate-research</p>
  </div>
</section>

<!-- Page 4: What to expect -->
<section class="page" style="left:322px;top:418px">
  <div class="topbar"><span class="doc">CHARITY GOLF DAY</span><span class="sec">SPONSORSHIP PROPOSAL</span><span class="num">4</span></div>
  <div class="abs" style="left:42px;top:52px;width:435px;font-size:7.7px;line-height:13.5px">
    <p class="blue" style="text-align:center;font-size:12px;font-weight:500;margin-bottom:18px">Friday 25 March 2022 at Elmwood Golf Club</p>
    <p>The Championship Par 72 layout of 6179 metres is a genuine test to all standards of players. Situated only 15 minutes from the city, the course meanders along the Yarra River providing a beautiful vista and is home for 100’s of species of native birds and tall-established trees.</p>
    <h3 class="sub" style="margin-top:14px">Breakfast :</h3>
    <ul class="flags"><li>Light Breakfast</li><li>Tea and coffee</li></ul>
    <h3 class="sub" style="margin-top:14px">Lunch :</h3>
    <ul class="flags"><li>Two-Course Lunch</li><li>Drinks at Bar Prices</li></ul>
    <h3 class="sub" style="margin-top:14px">What else to expect :</h3>
    <ul class="flags"><li>4-person Ambrose</li><li>On course competitions such as nearest the pins and longest drive</li><li>Trophies &amp; Prizes</li><li>On the day you will have access to practice putting, chipping greens, and driving range</li><li>A refreshment cart will circulate the golf course for players to purchase refreshments at own cost</li><li>Hire Equipment
      <ul class="dots" style="margin-left:4px"><li>Hire sets (Standard) $35.00 per set; (Premium) $50.00 per set</li><li>Hire shoes $10.00 per pair</li><li>Carts $40.00 each (Booking essential as numbers are limited, but it is an easy course to walk)</li></ul></li></ul>
    <h3 class="sub" style="margin-top:22px">Schedule :</h3>
    <div style="display:grid;grid-template-columns:100px 1fr">
      <span>7:00am to 7.30am</span><span>: Registration</span><span>7:15am</span><span>: Breakfast</span><span>7:45am</span><span>: Player Briefing</span><span>8:00am</span><span>: Shotgun start</span><span>12.30pm</span><span>: Lunch, Presentation/Prizes</span><span>3.00pm</span><span>: Finish</span>
    </div>
  </div>
</section>

<!-- Page 5: Sponsorship Gold/Silver -->
<section class="page" style="left:624px;top:418px">
  <div class="topbar"><span class="doc">CHARITY GOLF DAY</span><span class="sec">SPONSORSHIP PROPOSAL</span><span class="num">5</span></div>
  <div class="abs" style="left:42px;top:52px;width:435px;font-size:7.7px;line-height:13.5px">
    <div class="sechead">Sponsorship Opportunities</div>
    <p class="tier">Gold $5,000</p>
    <p>The Gold Sponsor is entitled to the following:</p>
    <ul class="flags"><li>Event naming rights</li><li>Eight (8) representatives playing in the event, including all green fees, four (4) carts, light breakfast &amp; 2 course lunch</li><li>our company signage / banners displayed exclusively at club entrance and social area.</li><li>Your logo and your company information on all promotional and marketing material being used on the day including our website, email to database and our social media channels.</li><li>A Banner with company logo on the first hole</li><li>Opportunity to say a few words at the beginning of the game as the chief sponsor of the event.</li><li>our company merchandise on display.</li><li>Presenting the winners awards</li><li>Free advertising in our Riverbend Club Newsletter, website, and social media channels for 12 months.</li><li>Opportunity to “capture” prospective clients on the day</li><li>Great Publicity: Be seen as being associated with an excellent cause</li></ul>
    <p class="tier" style="margin-top:20px">Silver $2,500</p>
    <p>The Silver Sponsor is entitled to the following:</p>
    <ul class="flags"><li>Four (4) representatives playing in the event, including all green fees, two (2) carts, light breakfast &amp; 2 course lunch</li><li>Exclusive banner with your company logo on a tee of choice (except hole 1)</li><li>Opportunity to say a few words as a major sponsor</li><li>Your company merchandise on display.</li><li>Your logo and your company information on all promotional and marketing material being used on the day including our website, email to database and our social media channels.</li><li>Free advertising in our Riverbend Club Newsletter, website, and social media channels for 6 months.</li><li>Opportunity to “capture” prospective clients on the day</li><li>Great Publicity: Be seen as being associated with an excellent cause</li></ul>
  </div>
</section>

<!-- Page 6: Bronze + payment -->
<section class="page" style="left:17px;top:801px">
  <div class="topbar"><span class="doc">CHARITY GOLF DAY</span><span class="sec">SPONSORSHIP PROPOSAL</span><span class="num">6</span></div>
  <div class="abs" style="left:42px;top:52px;width:435px;font-size:7.7px;line-height:13.5px">
    <div class="sechead">Sponsorship Opportunities</div>
    <p class="tier">Bronze $650</p>
    <p>This Bronze Sponsor is entitled to the following:</p>
    <ul class="flags"><li>Two (2) representatives playing in the event, including all green fees, light breakfast &amp; 2 course lunch</li><li>Exclusive banner with your company logo on a tee</li><li>Your logo and your company information on all promotional and marketing material being used on the day including our website, email to database and our social media channels.</li><li>Great Publicity: Be seen as being associated with an excellent cause</li><li>Opportunity to “capture” prospective clients on the day</li><li>Company merchandising display</li><li>Additional players - $150 per person (including all green fees, light breakfast &amp; 2-course lunch).</li></ul>
    <p class="tier" style="font-size:11.5px">Additional Players - $150 per person</p>
    <p>includes all green fees, light breakfast &amp; two (2) course lunch</p>
    <div class="sechead" style="margin-top:30px;font-size:12px">PAYMENT OPTIONS</div>
    <div style="display:grid;grid-template-columns:58px 1fr;margin-top:12px;row-gap:12px">
      <b style="font-weight:700">By Cheque</b><span>: Please make cheques payable to <b>The Riverbend Service Club</b><br>PO Box 42<br>Lakeside East, Vic 3999</span>
      <b style="font-weight:700">By Direct Deposit :</b><span><b>Account Name</b> : Riverbend Service Club<br><b>Bank</b> : Harbour Community Bank<br><b>BSB</b> : 111 222<br><b>Account Number</b> : 123 456 789<br><b>Comment</b> : RSCGolfDay/your name</span>
    </div>
    <div style="margin-top:14px;display:flex;gap:0"><b style="width:58px">By Credit Card :</b><span style="width:120px;padding-left:40px"><b>Nova</b> <span class="check" style="margin-left:6px"></span></span><span><b>Meridian</b> <span class="check" style="margin-left:6px"></span></span></div>
    <div style="margin-left:58px;margin-top:6px;line-height:21px">
      <div style="display:flex;justify-content:space-between;width:330px"><span>Card No. ____ ____ ____ ____</span><span>Expiry __ / __</span></div>
      <div class="field" style="width:245px;margin:0"><span>Cardholder’s Name:</span><span class="line"></span></div>
      <div style="display:flex;gap:10px;width:380px"><div class="field" style="flex:0 0 245px;margin:0"><span>Cardholder’s Signature:</span><span class="line"></span></div><div class="field" style="flex:1;margin:0"><span>Date:</span><span class="line"></span></div></div>
    </div>
  </div>
</section>

<!-- Page 7: Form part 1 -->
<section class="page" style="left:322px;top:801px">
  <div class="topbar"><span class="doc">CHARITY GOLF DAY</span><span class="sec">SPONSORSHIP PROPOSAL</span><span class="num">7</span></div>
  <div class="abs" style="left:42px;top:52px;width:435px">
    <div class="sechead">Sponsorship Package: (Please Tick)</div>
    <div style="display:flex;justify-content:space-between;font-size:7.6px;font-weight:600;margin-top:28px"><span><span class="check"></span>Gold ($5,000)</span><span><span class="check"></span>Silver ($2,500)</span><span><span class="check"></span>Bronze ($650)</span><span><span class="check"></span>Additional Players ($150)</span></div>
    <div style="display:flex;justify-content:flex-end;align-items:center;gap:4px;font-size:7.6px;margin:12px 45px 4px 0">No: <span style="width:70px;height:12px;border:1px solid #444"></span></div>
    <div class="field"><span>Company:</span><span class="line"></span></div>
    <div class="field"><span>Address:</span><span class="line"></span></div>
    <div class="field"><span>Suburb:</span><span class="line" style="flex:0 0 235px"></span><span style="margin-left:6px">P/Code:</span><span class="line"></span></div>
    <div class="field"><span>Mobile:</span><span class="line"></span></div>
    <div class="field"><span>Contact Name:</span><span class="line"></span></div>
    <div class="field"><span>Contact Email:</span><span class="line"></span></div>
    <p class="blue" style="font-size:9.5px;font-weight:600;margin:28px 0 10px">Team Name:</p>
    <div class="player">
      <div class="field"><b>Player 1:</b><span class="line"></span></div><div class="field short" style="margin-bottom:32px"><span>Official GA H/Cap:</span><span class="line"></span></div>
      <div class="field"><b>Player 2:</b><span class="line"></span></div><div class="field short" style="margin-bottom:32px"><span>Official GA H/Cap:</span><span class="line"></span></div>
      <div class="field"><b>Player 3:</b><span class="line"></span></div><div class="field short" style="margin-bottom:32px"><span>Official GA H/Cap:</span><span class="line"></span></div>
      <div class="field"><b>Player 4:</b><span class="line"></span></div><div class="field short" style="margin-bottom:22px"><span>Official GA H/Cap:</span><span class="line"></span></div>
    </div>
    <p class="note"><b>Please Note</b>: Any player without an official GA H/Cap will be given a maximum handicap of 27 (Males) &amp; 36 (Females).</p>
  </div>
</section>

<!-- Page 8: Form part 2 -->
<section class="page" style="left:624px;top:801px">
  <div class="topbar"><span class="doc">CHARITY GOLF DAY</span><span class="sec">SPONSORSHIP PROPOSAL</span><span class="num">8</span></div>
  <div class="abs" style="left:42px;top:52px;width:435px">
    <div class="sechead">Sponsorship Package: (Please Tick)</div>
    <p class="blue" style="font-size:9.5px;font-weight:600;margin:20px 0 8px">Team Name:</p>
    <div class="player">
      <div class="field"><b>Player 5:</b><span class="line"></span></div><div class="field short" style="margin-bottom:32px"><span>Official GA H/Cap:</span><span class="line"></span></div>
      <div class="field"><b>Player 6:</b><span class="line"></span></div><div class="field short" style="margin-bottom:32px"><span>Official GA H/Cap:</span><span class="line"></span></div>
      <div class="field"><b>Player 7:</b><span class="line"></span></div><div class="field short" style="margin-bottom:32px"><span>Official GA H/Cap:</span><span class="line"></span></div>
      <div class="field"><b>Player 8:</b><span class="line"></span></div><div class="field short" style="margin-bottom:22px"><span>Official GA H/Cap:</span><span class="line"></span></div>
    </div>
    <p class="note"><b>Please Note</b>: Any player without an official GA H/Cap will be given a maximum handicap of 27 (Males) &amp; 36 (Females).</p>
  </div>
  <div class="cornerbox" style="left:48px;top:416px;width:418px;height:172px"><i class="tl"></i><i class="tr"></i><i class="bl"></i><i class="br"></i>
    <p class="green" style="text-align:center;font-size:9.5px;font-weight:600;margin-top:18px">Cancellation Terms</p>
    <p style="font-size:7.5px;line-height:16.5px;padding:4px 10px 0;text-align:justify">If the organiser cancels the event prior to the scheduled date, the sponsor is entitled to a 100% refund. If the event is rescheduled by the organiser, and the player or sponsor can reasonably demonstrate their inability to participate they will be entitled to a full refund. In the event of a player or sponsor cancellation, the Riverbend Service Club reserves the right to retain monies paid in full unless resold. Any cancellations must be advised in writing via email to the Convenor Mara Ellison (mara.ellison@mailbox.example).</p>
  </div>
</section>

</body>
</html>
```